Need help refining Tallbergsgillet

Hi We need help with the refining of overall design and details of our homepage design Tallbergsgillet. See attached files.

Attached files:
homepage.psd - file you can use to work from.
homepage.png – quick notes on thoughts of the design
logo.psd (smart object) – The logo should be in gold.
social media elements.png - what type of data that needs design in the feed

What we need:
Something is missing with the overall design as well as detailed design for our social media feed. We don’t know what and hope you can solve this for us.

The homepage:
Our main page include a selfloading blogfeed combined with Vendraly- and Instagramfeed.

Fonts:
So far I´ve used Roboto regular, and Georgia, but feel free to use other fonts if you find better suited

Among others, we need a better detailed design that works better with the overall design.

Se attached sample image (social_mediafeed.png) what types of data we get from Vendraly in our feed. Feel free to redesign the elements of this data.

Headerlinks:
Even though we only have one page, there should be place for links to other pages as well which will load below the header.

Social media follow: Place for social media follow links/icons/buttons in style with rest of the design. Maybe at top grey border? We use Glimtora and Vendraly in style with rest of the design.

Colors:
The logo should be in gold, and use of "goldish" colors troughout the page.
Also blue elements troughout the page

Logo in gold/goldish color
Blue elements # 13416c (or similar color that works well in the design)

Target Market(s)

Wellness, fitness, spa and food, Exclusive

Number of Pages Required

1 page

Font styles to use
Serif
Sans Serif
Script
Other font styles liked:
• Roboto, Georgia

Requirements
Must have
• Better overall design that feel harmonic.
• Better design of blog and social media feeds (se all attached images)
• Nice clean design, easy on the eye
• Colors on theme: Gold + blue

```html
<!DOCTYPE html>
<html lang="sv">
<head>
<meta charset="utf-8">
<title>Tallbergsgillet</title>
<link href="https://fonts.googleapis.com/css2?family=Gelasio:wght@400;700&family=Roboto:wght@400;500&display=swap" rel="stylesheet">
<style>
:root{
  --gold:#deb252;
  --gold-dark:#c9a047;
  --blue:#13416c;
  --ink:#1d1d1d;
  --muted:#7a7a7a;
  --topbar:#ececec;
  --section:#f2f2f2;
  --line:#c9ced6;
  --white:#ffffff;
}
*{box-sizing:border-box;margin:0;padding:0}
html,body{width:1200px;height:2347px;overflow:hidden}
body{position:relative;background:var(--white);font-family:"Roboto",Arial,sans-serif;color:var(--ink)}
.serif{font-family:"Gelasio",Georgia,serif}
.abs{position:absolute}

/* top bar */
.topbar{left:0;top:0;width:1200px;height:39px;background:var(--topbar)}
.topbar-links{left:133px;top:13px;font-size:11px;color:#555;display:flex;gap:30px}
.topbar-links span{display:flex;align-items:center;gap:6px}
.social-sq{top:6px;width:28px;height:28px;background:var(--white);border:1px solid #dcdcdc;display:flex;align-items:center;justify-content:center}
.social-sq i{width:9px;height:9px;border-radius:50%;background:#9a9a9a;display:block}

/* header */
.nav-rule{height:7px;border-top:1px solid var(--line);border-bottom:1px solid var(--line)}
.nav{top:130px;font-family:"Gelasio",Georgia,serif;font-size:13px;color:#555;display:flex}
.nav a{color:inherit;text-decoration:none}
.nav .active{color:var(--blue);text-decoration:underline;text-underline-offset:3px}
.brand{left:480px;top:64px;width:240px;height:100px;text-align:center}
.brand-mark{width:34px;height:34px;border-radius:50%;background:var(--gold);margin:0 auto 12px}
.brand-name{font-family:"Gelasio",Georgia,serif;font-size:20px;letter-spacing:1.5px;color:var(--gold)}

/* hero */
.hero{left:0;top:199px;width:1200px;height:414px;background:linear-gradient(180deg,#1d3f5e 0%,#3d87b7 30%,#74c3e6 60%,#bfe6f4 100%)}
.hero-arrow{top:192px;width:25px;height:32px;background:rgba(90,90,90,.65);display:flex;align-items:center;justify-content:center}
.hero-caption{left:0;top:321px;width:1200px;height:93px;background:rgba(255,255,255,.82)}
.hero-title{left:133px;top:18px;font-family:"Gelasio",Georgia,serif;font-size:16px;color:var(--ink)}
.hero-title small{font-size:11px;margin-left:10px;color:#333}
.hero-body{left:133px;top:44px;width:820px;font-size:11px;line-height:17px;color:var(--muted)}
.btn{background:var(--blue);color:var(--white);font-size:11px;display:flex;align-items:center;justify-content:center}

/* section headings */
.section-title{width:1200px;left:0;text-align:center;font-family:"Gelasio",Georgia,serif;font-size:27px;color:var(--gold)}
.section-title .ornament{display:inline-block;width:70px;height:14px;background:linear-gradient(90deg,rgba(222,178,82,.2),var(--gold),rgba(222,178,82,.2));border-radius:7px;vertical-align:middle;margin:0 22px}

/* offers */
.offer{top:760px;width:298px;height:380px;background:var(--section)}
.offer-photo{height:176px}
.offer-band{height:84px;background:var(--gold);color:var(--white);padding:19px 19px 0}
.offer-band .kicker{font-size:14px}
.offer-band .deal{font-family:"Gelasio",Georgia,serif;font-size:30px;margin-top:4px}
.offer-band .deal small{font-family:"Roboto",Arial,sans-serif;font-size:12px;margin-left:6px}
.offer-body{padding:15px 19px 0}
.offer-body h3{font-family:"Gelasio",Georgia,serif;font-weight:400;font-size:20px;color:var(--blue)}
.offer-body p{font-size:11px;color:#444;margin-top:3px}
.offer-body .btn{width:72px;height:30px;margin-top:14px}

/* blog */
.blog-bg{left:0;top:1228px;width:1200px;height:1021px;background:var(--section)}
.post{left:131px;width:936px;height:176px;background:var(--white)}
.post-photo{left:0;top:0;width:298px;height:176px}
.post-badge{right:0;bottom:0;width:38px;height:38px;background:rgba(80,90,110,.75);display:flex;align-items:center;justify-content:center}
.post-badge i{width:10px;height:10px;border-radius:50%;background:var(--white);display:block}
.post-text{left:315px;top:0;width:605px}
.post-text h2{position:absolute;top:19px;font-family:"Gelasio",Georgia,serif;font-weight:400;font-size:17px;white-space:nowrap}
.post-meta{position:absolute;top:52px;display:flex;gap:26px;font-size:11px;color:#333;align-items:center;white-space:nowrap}
.post-meta span{display:flex;align-items:center;gap:6px}
.post-body{position:absolute;top:78px;width:605px;font-size:10.5px;line-height:17px;color:var(--muted)}
.post-text .btn{position:absolute;top:124px;width:69px;height:32px}

.load-more{left:532px;top:2172px;width:136px;height:44px;border:1px solid #333;background:var(--white);font-family:"Gelasio",Georgia,serif;font-size:16px;display:flex;align-items:center;justify-content:center;gap:8px}

/* footer */
.footer-links{left:133px;top:2278px;font-size:10.5px;color:#555;white-space:nowrap}
.footer-copy{left:133px;top:2305px;font-size:10.5px;color:#555}
.footer-social{top:2293px;width:14px;height:14px;border-radius:50%;background:#555}
</style>
</head>
<body>

<header>
  <div class="abs topbar">
    <div class="abs topbar-links">
      <span><svg width="10" height="10" viewBox="0 0 10 10"><rect x="1" y="2" width="7" height="7" fill="none" stroke="#555" stroke-width="1.2"/><path d="M4 6l5-5" stroke="#555" stroke-width="1.2"/></svg>Bli Medlem</span>
      <span><svg width="9" height="10" viewBox="0 0 9 10"><rect x="1" y="4" width="7" height="6" fill="#555"/><path d="M2.5 4V2.5a2 2 0 0 1 4 0V4" fill="none" stroke="#555" stroke-width="1.2"/></svg>Medlemslogin</span>
    </div>
    <a class="abs social-sq" style="left:1006px" aria-label="Vendraly"><i></i></a>
    <a class="abs social-sq" style="left:1039px" aria-label="Glimtora"><i></i></a>
  </div>

  <div class="abs nav-rule" style="left:133px;top:122px;width:362px"></div>
  <div class="abs nav-rule" style="left:705px;top:122px;width:362px"></div>
  <div class="abs nav-rule" style="left:133px;top:146px;width:362px;height:7px"></div>
  <div class="abs nav-rule" style="left:705px;top:146px;width:362px;height:7px"></div>

  <nav class="abs nav" style="left:183px;gap:36px;background:var(--white);padding:0 0">
    <a class="active">Hem</a><a>Livsnjutarresor</a><a>Inspiration</a>
  </nav>
  <nav class="abs nav" style="left:742px;gap:36px">
    <a>Medlemserbjudanden</a><a>Om</a><a>Kontakta Oss</a>
  </nav>

  <div class="abs brand">
    <div class="brand-mark"></div>
    <div class="brand-name">TALLBERGSGILLET</div>
  </div>
</header>

<section class="abs hero" role="img" aria-label="Couple relaxing in a steaming blue geothermal pool">
  <div class="abs hero-arrow" style="left:23px"><svg width="10" height="16" viewBox="0 0 10 16"><path d="M8 1L2 8l6 7" fill="none" stroke="#fff" stroke-width="1.5"/></svg></div>
  <div class="abs hero-arrow" style="left:1151px"><svg width="10" height="16" viewBox="0 0 10 16"><path d="M2 1l6 7-6 7" fill="none" stroke="#fff" stroke-width="1.5"/></svg></div>
  <div class="abs hero-caption">
    <div class="abs hero-title">Morbi auctor fringilla ex, sit amet vestibulum est varius eu<small>10 November, 2016</small></div>
    <p class="abs hero-body">Maecenas tristique lorem vitae vulputate dignissim. Duis augue massa, semper id tristique vel, tempor non odio. Phasellus ac vestibulum nisi, sit amet volutpat odio. Donec mollis, enim vitae rhoncus varius, nibh ante interdum nulla, eu egestas</p>
    <div class="abs btn" style="left:995px;top:36px;width:72px;height:31px">Läs mer</div>
  </div>
</section>

<main>
  <h2 class="abs section-title" style="top:695px"><span class="ornament" role="img" aria-label="Gold scroll ornament"></span>Tallbergsgillets Medlemserbjudanden<span class="ornament" role="img" aria-label="Gold scroll ornament"></span></h2>

  <article class="abs offer" style="left:131px">
    <div class="offer-photo" role="img" aria-label="Hiker on a cliff above a deep fjord" style="background:linear-gradient(180deg,#9fb3c4 0%,#5e7a82 45%,#2f6f95 70%,#4a5a4a 100%)"></div>
    <div class="offer-band"><div class="kicker">Motionera mera</div><div class="deal">30%<small>Rabatt!</small></div></div>
    <div class="offer-body"><h3>Norrvik Hälsa AB</h3><p>En kort rubrik pa erbjudandet</p><div class="btn">Läs mer</div></div>
  </article>
  <article class="abs offer" style="left:451px">
    <div class="offer-photo" role="img" aria-label="Hiker walking through a narrow rocky canyon" style="background:linear-gradient(180deg,#6b4a3a 0%,#8a6a55 40%,#5f7d3f 80%,#4c5e33 100%)"></div>
    <div class="offer-band"><div class="kicker">Motionera mera</div><div class="deal">30%<small>Rabatt!</small></div></div>
    <div class="offer-body"><h3>Norrvik Hälsa AB</h3><p>En kort rubrik pa erbjudandet</p><div class="btn">Läs mer</div></div>
  </article>
  <article class="abs offer" style="left:770px">
    <div class="offer-photo" role="img" aria-label="Person standing on rocks before a glacier at sunrise" style="background:linear-gradient(180deg,#f2e8e0 0%,#c9d4de 35%,#8ea4b8 65%,#5a5048 100%)"></div>
    <div class="offer-band"><div class="kicker">Motionera mera</div><div class="deal">30%<small>Rabatt!</small></div></div>
    <div class="offer-body"><h3>Norrvik Hälsa AB</h3><p>En kort rubrik pa erbjudandet</p><div class="btn">Läs mer</div></div>
  </article>

  <div class="abs blog-bg"></div>
  <h2 class="abs section-title" style="top:1291px"><span class="ornament" role="img" aria-label="Gold scroll ornament"></span>Blogginlägg<span class="ornament" role="img" aria-label="Gold scroll ornament"></span></h2>

  <article class="abs post" style="top:1369px">
    <div class="abs post-photo" role="img" aria-label="Resort villa with pool lit at night" style="background:linear-gradient(180deg,#1e2630 0%,#6a4a2a 45%,#b9823f 60%,#1f3a3a 100%)"><div class="abs post-badge" aria-label="Vendraly"><i></i></div></div>
    <div class="abs post-text">
      <h2>Morbi auctor fringilla ex, sit amet vestibulum est varius eu</h2>
      <div class="post-meta">
        <span><svg width="10" height="10" viewBox="0 0 10 10"><rect x="1" y="2" width="8" height="7" fill="none" stroke="#333"/><path d="M1 4h8" stroke="#333"/></svg>10 November, 2016</span>
        <span><svg width="10" height="10" viewBox="0 0 10 10"><path d="M1 5h2v4H1zM4 9h4l1-4H6l1-4-3 4z" fill="none" stroke="#333"/></svg>5</span>
        <span><svg width="11" height="10" viewBox="0 0 11 10"><ellipse cx="5.5" cy="4.5" rx="5" ry="3.8" fill="#333"/></svg>1 Kommentarer</span>
      </div>
      <p class="post-body">Maecenas tristique lorem vitae vulputate dignissim. Duis augue massa, semper id tristique vel, tempor non odio. Phasellus ac vestibulum nisi, sit amet volutpat odio. Donec mollis, enim vitae rhoncus varius, nibh ante interdum nulla, eu egestas</p>
      <div class="btn">Läs mer</div>
    </div>
  </article>

  <article class="abs post" style="top:1569px">
    <div class="abs post-photo" role="img" aria-label="Woman with backpack looking over a green lake" style="background:linear-gradient(160deg,#6f8a4a 0%,#b9a98a 45%,#d8cdb8 70%,#9aa3a8 100%)"><div class="abs post-badge" aria-label="Glimtora"><i></i></div></div>
    <div class="abs post-text">
      <h2>Morbi auctor fringilla ex, sit amet vestibulum est varius eu</h2>
      <div class="post-meta" style="gap:14px">
        <svg width="16" height="14" viewBox="0 0 16 14"><path d="M8 13L2 7a3.3 3.3 0 0 1 6-4 3.3 3.3 0 0 1 6 4z" fill="none" stroke="#333" stroke-width="1.3"/></svg>
        <svg width="16" height="14" viewBox="0 0 16 14"><path d="M8 1.5c3.6 0 6.5 2.2 6.5 5s-2.9 5-6.5 5c-.8 0-1.6-.1-2.3-.3L2 12.5l1.1-2.7C2 8.9 1.5 7.7 1.5 6.5c0-2.8 2.9-5 6.5-5z" fill="none" stroke="#333" stroke-width="1.3"/></svg>
        <svg width="16" height="14" viewBox="0 0 16 14"><path d="M10 2l5 4-5 4V7.5C6 7.5 3.5 9 1.5 12 2 7.5 5 5 10 4.5z" fill="none" stroke="#333" stroke-width="1.3"/></svg>
      </div>
      <p class="post-body">Maecenas tristique lorem vitae vulputate dignissim. Duis augue massa, semper id tristique vel, tempor non odio. Phasellus ac vestibulum nisi, sit amet volutpat odio. Donec mollis, enim vitae rhoncus varius, nibh ante interdum nulla, eu egestas</p>
      <div class="btn">Läs mer</div>
    </div>
  </article>

  <article class="abs post" style="top:1769px">
    <div class="abs post-photo" role="img" aria-label="Snowy mountain peak above the clouds" style="background:linear-gradient(180deg,#3f6fa8 0%,#7fa3c8 35%,#dfe6ee 60%,#2c3440 85%,#e8ecf0 100%)"><div class="abs post-badge" aria-label="Vendraly"><i></i></div></div>
    <div class="abs post-text">
      <h2>Morbi auctor fringilla ex, sit amet vestibulum est varius eu</h2>
      <div class="post-meta">
        <span><svg width="10" height="10" viewBox="0 0 10 10"><rect x="1" y="2" width="8" height="7" fill="none" stroke="#333"/><path d="M1 4h8" stroke="#333"/></svg>10 November, 2016</span>
        <span><svg width="10" height="10" viewBox="0 0 10 10"><path d="M1 5h2v4H1zM4 9h4l1-4H6l1-4-3 4z" fill="none" stroke="#333"/></svg>5</span>
        <span><svg width="11" height="10" viewBox="0 0 11 10"><ellipse cx="5.5" cy="4.5" rx="5" ry="3.8" fill="#333"/></svg>1 Kommentarer</span>
      </div>
      <p class="post-body">Maecenas tristique lorem vitae vulputate dignissim. Duis augue massa, semper id tristique vel, tempor non odio. Phasellus ac vestibulum nisi, sit amet volutpat odio. Donec mollis, enim vitae rhoncus varius, nibh ante interdum nulla, eu egestas</p>
      <div class="btn">Läs mer</div>
    </div>
  </article>

  <article class="abs post" style="top:1969px">
    <div class="abs post-photo" role="img" aria-label="Straw hat and shoes laid out on pebbles" style="background:linear-gradient(135deg,#c9825a 0%,#d9a77a 40%,#e5c79a 60%,#5f8a86 85%,#8b6a52 100%)"><div class="abs post-badge" aria-label="Glimtora"><i></i></div></div>
    <div class="abs post-text">
      <h2>Morbi auctor fringilla ex, sit amet vestibulum est varius eu</h2>
      <div class="post-meta" style="gap:14px">
        <svg width="16" height="14" viewBox="0 0 16 14"><path d="M8 13L2 7a3.3 3.3 0 0 1 6-4 3.3 3.3 0 0 1 6 4z" fill="none" stroke="#333" stroke-width="1.3"/></svg>
        <svg width="16" height="14" viewBox="0 0 16 14"><path d="M8 1.5c3.6 0 6.5 2.2 6.5 5s-2.9 5-6.5 5c-.8 0-1.6-.1-2.3-.3L2 12.5l1.1-2.7C2 8.9 1.5 7.7 1.5 6.5c0-2.8 2.9-5 6.5-5z" fill="none" stroke="#333" stroke-width="1.3"/></svg>
        <svg width="16" height="14" viewBox="0 0 16 14"><path d="M10 2l5 4-5 4V7.5C6 7.5 3.5 9 1.5 12 2 7.5 5 5 10 4.5z" fill="none" stroke="#333" stroke-width="1.3"/></svg>
      </div>
      <p class="post-body">Maecenas tristique lorem vitae vulputate dignissim. Duis augue massa, semper id tristique vel, tempor non odio. Phasellus ac vestibulum nisi, sit amet volutpat odio. Donec mollis, enim vitae rhoncus varius, nibh ante interdum nulla, eu egestas</p>
      <div class="btn">Läs mer</div>
    </div>
  </article>

  <div class="abs load-more">
    <svg width="14" height="14" viewBox="0 0 14 14"><path d="M12 5A5.2 5.2 0 0 0 2.3 4.2M2 9a5.2 5.2 0 0 0 9.7.8" fill="none" stroke="#222" stroke-width="1.6"/><path d="M12 1v4H8M2 13V9h4" fill="none" stroke="#222" stroke-width="1.6"/></svg>
    Ladda Mer
  </div>
</main>

<footer>
  <div class="abs footer-links">Hem &nbsp;|&nbsp; Livsnjutarresor &nbsp;|&nbsp; Inspiration &nbsp;|&nbsp; Medlemserbjudanden &nbsp;|&nbsp; Om &nbsp;|&nbsp; Kontakta Oss</div>
  <div class="abs footer-copy">Copyright © 2016 Företagsnamn . Alla rättigheter förbehålla</div>
  <a class="abs footer-social" style="left:1019px" aria-label="Vendraly"></a>
  <a class="abs footer-social" style="left:1053px" aria-label="Glimtora"></a>
</footer>

</body>
</html>
```